Bref créative
Bath/Spa Product Label
Vesta Reef
Thanks to you expert graphic artists we have been happy with the logo designed last summer and would like to see what you wizards can do to with a product label.
We have attached the current logo and would love to see what you can do with creating a product label that will fit several types of labels.
1. We need a vertical orientation of the label to be scalable so that we can use it on 16 oz or 8 ounce bottles.
2. We need a horizontal orientation that is also scalable for 8 ounce or 4 ounce jars.
You can place the uploaded logo anywhere on the labels but we need blank space to fill in the product name, net weight, instructions and ingredients.
Feel free to apply generic text for the net weight, instructions and ingredients. We manufacture shampoos, conditioners, body washes, shower gels, body scrubs, foot scrubs, sugar scrubs, etc.
We have attached two sample MS Word documents with the ugly and boring labels we use now. Use these as inspiration to move us to the next level. Go ahead add color, fonts, additional graphics - whatever you see fit. In the past, we have treated our designers fairly and cordially. You can expect the same treatment for this contest.
Personal Care
Over 95% of our customer base is women. But keep in mind that men also use shower gels - so no teddy bears on the product label please.Our clients are used to high quality product, not over hyped claims or garish designs.
As stated above we need the label in at least two orientations. It must also be scalable so that we can use it on different size labels. If you can design a third label in square dimensions that would be a big bonus.
Current jar label - for example DO NOT REPLICATE.
Sample shampoo/body wash label applied vertically to 16 ounce or 8 ounce bottles. FOR EXAMPLE ONLY DO NOT REPLICATE
Current logo - DO NOT DISTRIBUTE - COPYRIGHT VESTA REEF.

```html
<!DOCTYPE html>
<html lang="en">
<head>
<meta charset="utf-8">
<title>Vesta Reef – Sugar Scrub Labels</title>
<link rel="stylesheet" href="https://fonts.googleapis.com/css2?family=Cinzel:wght@400;500&family=Quicksand:wght@400;600&display=swap">
<style>
  :root{
    --bg:#e7e8e9;
    --gold-dark:#b98f34;
    --gold:#d2ad55;
    --gold-light:#ecd591;
    --cream:#fbf7e4;
    --blue:#2f5f92;
    --blue-light:#6f9ccc;
    --ink-gold:#b48a2c;
    --navy:#1f4a78;
    --white:#ffffff;
    --warn:#f3dc3a;
  }
  *{box-sizing:border-box;margin:0;padding:0}
  html,body{width:1200px;height:897px;overflow:hidden;background:var(--bg)}
  .canvas{position:relative;width:1200px;height:897px}

  /* Horizontal jar label */
  .jar-label{
    position:absolute;left:96px;top:91px;width:1008px;height:207px;
    background:linear-gradient(90deg,var(--gold-dark) 0%,var(--gold) 30%,var(--gold-light) 55%,var(--gold) 80%,var(--gold-dark) 100%);
  }
  .jar-label::before,.jar-label::after{
    content:"";position:absolute;left:0;right:0;height:6px;
    background:linear-gradient(90deg,var(--blue) 0%,var(--blue-light) 12%,transparent 30%,transparent 70%,var(--blue-light) 88%,var(--blue) 100%);
  }
  .jar-label::before{top:0}
  .jar-label::after{bottom:0}
  .jar-blurb{
    position:absolute;left:10px;top:28px;width:290px;
    font-family:"Quicksand",sans-serif;font-size:13.5px;line-height:1.42;color:var(--white);
    text-align:right;letter-spacing:.2px;
  }
  .jar-net{
    position:absolute;right:724px;top:174px;
    font-family:"Quicksand",sans-serif;font-size:9px;color:var(--white);
  }
  .jar-panel{
    position:absolute;left:307px;top:6px;width:394px;height:195px;
    background:var(--cream);border-radius:44px;text-align:center;
  }
  .jar-name{
    margin-top:50px;
    font-family:"Cinzel",serif;font-weight:400;font-size:44px;letter-spacing:2px;color:var(--ink-gold);line-height:1;
  }
  .jar-product{
    margin-top:10px;font-family:"Cinzel",serif;font-size:13px;line-height:1.35;color:var(--navy);letter-spacing:.4px;
  }
  .jar-flourish{
    width:120px;height:14px;margin:8px auto 0;border-radius:7px;
    background:linear-gradient(90deg,transparent,var(--gold-light),var(--gold),var(--gold-light),transparent);
    opacity:.7;
  }
  .jar-url{
    margin-top:16px;font-family:"Quicksand",sans-serif;font-size:8px;color:var(--navy);
  }
  .jar-ingredients{
    position:absolute;left:720px;top:36px;width:280px;
    font-family:"Quicksand",sans-serif;color:var(--white);
  }
  .jar-ingredients h3{font-family:"Cinzel",serif;font-weight:400;font-size:12px;letter-spacing:1px;margin-bottom:2px}
  .jar-ingredients p{font-size:11px;line-height:1.4;text-align:justify}
  .jar-warning{
    position:absolute;left:720px;top:111px;width:280px;padding:6px 10px;
    background:var(--warn);border-radius:8px;
    font-family:"Quicksand",sans-serif;font-size:10px;line-height:1.35;color:var(--white);
  }
  .jar-warning strong{color:#c0392b;font-weight:600}

  /* Square label */
  .square-label{
    position:absolute;left:336px;top:348px;width:492px;height:492px;
    background:linear-gradient(135deg,var(--gold-light) 0%,var(--gold) 35%,var(--gold-dark) 60%,var(--gold-light) 100%);
    padding:20px;
  }
  .square-inner{
    position:relative;width:100%;height:100%;background:var(--cream);
  }
  .square-inner::before{
    content:"";position:absolute;inset:14px;border:2px solid var(--gold);
  }
  .square-mark{
    position:absolute;left:50%;top:88px;width:64px;height:64px;margin-left:-32px;
    border-radius:50%;background:var(--gold);
  }
  .square-name{
    position:absolute;left:0;right:0;top:176px;text-align:center;
    font-family:"Cinzel",serif;font-weight:400;font-size:52px;letter-spacing:3px;color:var(--ink-gold);line-height:1;
  }
  .square-product{
    position:absolute;left:0;right:0;top:246px;text-align:center;
    font-family:"Cinzel",serif;font-weight:500;font-size:30px;letter-spacing:1px;color:var(--navy);
  }
  .square-url{
    position:absolute;left:0;right:0;top:410px;text-align:center;
    font-family:"Quicksand",sans-serif;font-size:9px;color:var(--navy);
  }
</style>
</head>
<body>
<main class="canvas">
  <section class="jar-label">
    <p class="jar-blurb">A unique blend of safflower oil, sugar and Jojoba beads, to exfoliate and bring a lovely glow to your skin. Scented with invigorating Lavender Mint.</p>
    <p class="jar-net">Net: 8 ounce</p>
    <div class="jar-panel">
      <h1 class="jar-name">VESTA REEF</h1>
      <p class="jar-product">Glistening Sugar Scrub<br>with Jojoba Beads and Lavender Mint Scent</p>
      <div class="jar-flourish" role="img" aria-label="Decorative gold flourish"></div>
      <p class="jar-url">www.vestareef.com</p>
    </div>
    <div class="jar-ingredients">
      <h3>INGREDIENTS</h3>
      <p>Sucrose, Carthamus Tinctorius (Safflower) Seed Oil, Polysorbate 80, Tocopheryl Acetate (Vitamin E), Fragrance, Silica, Phenoxyethanol</p>
    </div>
    <p class="jar-warning"><strong>WARNING:</strong> This product contains natural oils that can make surfaces slippery. Use caution whenever using this product to prevent possible injury.</p>
  </section>

  <section class="square-label">
    <div class="square-inner">
      <div class="square-mark" aria-hidden="true"></div>
      <h2 class="square-name">VESTA REEF</h2>
      <p class="square-product">SUGAR SCRUB</p>
      <p class="square-url">www.vestareef.com</p>
    </div>
  </section>
</main>
</body>
</html>
```